Business card for a shipping supplies business

Needing a business card design. Please see the logo. The logo with the white font should be used if there is a dark background.

We are looking for the following info on the card. Please see the sample info. We will need the info to be changed with a few different employee names and info but all will use the same template.

Business Name: The Crate Heron
Employee Name : Marcus Delaney
Position: Account Manager
Address: 4827 W. Ridge 418 S.
Fort Worth, TX 73948
email: Marcus@thecrateheron.example
telephone: 855-619-2740 x 207
website: www.getparcelkits.example

Target Market(s)

Businesses who ship products for online sales

Industry/Entity Type

Cardboard

Contact Information for Business Card

Name, title, address, website, logo, telephone number

Font styles to use
Sans Serif

Colors
EE7325
F08F49
F5BC92
FAE3D3
FDF4ED

Requirements
Must have
• Logo on back of card. Clean look, just logo, website address

```html
<!DOCTYPE html>
<html lang="en">
<head>
<meta charset="UTF-8">
<title>The Crate Heron – Business Card</title>
<link href="https://fonts.googleapis.com/css2?family=Open+Sans:wght@400;600;700&display=swap" rel="stylesheet">
<style>
  :root {
    --backdrop: #3a9aae;
    --card-light: #ffffff;
    --card-dark: #141414;
    --ink: #1a1a1a;
    --orange: #d9591f;
    --orange-brief: #ee7325;
    --white: #ffffff;
  }
  * { margin: 0; padding: 0; box-sizing: border-box; }
  html, body {
    width: 1108px;
    height: 1200px;
    overflow: hidden;
    background: var(--backdrop);
    font-family: "Open Sans", Arial, sans-serif;
  }
  .canvas {
    position: relative;
    width: 1108px;
    height: 1200px;
  }
  .card {
    position: absolute;
    left: 104px;
    width: 900px;
    height: 514px;
    box-shadow: 0 3px 8px rgba(0,0,0,0.25);
  }
  .card-front { top: 60px; background: var(--card-light); }
  .card-back { top: 626px; background: var(--card-dark); }

  .brand {
    position: absolute;
    display: flex;
    align-items: center;
    gap: 12px;
    font-weight: 700;
    font-size: 30px;
    letter-spacing: 0.5px;
    white-space: nowrap;
  }
  .brand-square {
    width: 26px;
    height: 26px;
    background: var(--orange);
    flex: none;
  }
  .card-front .brand { left: 64px; top: 226px; color: var(--ink); }
  .card-back .brand {
    left: 50%;
    top: 50%;
    transform: translate(-50%, -50%);
    color: var(--white);
  }

  .divider {
    position: absolute;
    left: 450px;
    top: 180px;
    width: 2px;
    height: 156px;
    background: var(--orange);
  }
  .contact {
    position: absolute;
    left: 482px;
    top: 176px;
    color: var(--ink);
  }
  .contact-name {
    font-size: 24px;
    font-weight: 600;
    line-height: 1.1;
  }
  .contact-title {
    font-size: 15px;
    line-height: 1.3;
    margin-bottom: 22px;
  }
  .contact-list { list-style: none; }
  .contact-list li {
    display: flex;
    align-items: center;
    gap: 10px;
    font-size: 17px;
    line-height: 1.9;
  }
  .contact-list svg { width: 13px; height: 13px; flex: none; }

  .address {
    position: absolute;
    left: 0;
    right: 0;
    top: 462px;
    text-align: center;
    font-size: 17px;
    color: var(--ink);
  }
</style>
</head>
<body>
<main class="canvas">
  <section class="card card-front" aria-label="Card front">
    <div class="brand"><span class="brand-square"></span>The Crate Heron</div>
    <div class="divider"></div>
    <div class="contact">
      <p class="contact-name">Marcus Delaney</p>
      <p class="contact-title">Account Manager</p>
      <ul class="contact-list">
        <li>
          <svg viewBox="0 0 16 16" aria-hidden="true"><path fill="#d9591f" d="M3.6 1.2 6 3.6 4.6 5.6c.9 2 2.6 3.7 4.6 4.6l2-1.4 2.4 2.4-1.6 2.2C6.6 13.6 1.2 8.2 1.4 2.8z"/></svg>
          855-619-2740 x 207
        </li>
        <li>
          <svg viewBox="0 0 16 16" aria-hidden="true"><rect x="1" y="3" width="14" height="10" fill="#d9591f"/><path d="M1.5 3.5 8 9l6.5-5.5" fill="none" stroke="#fff" stroke-width="1.3"/></svg>
          Marcus@thecrateheron.example
        </li>
        <li>
          <svg viewBox="0 0 16 16" aria-hidden="true"><g fill="none" stroke="#d9591f" stroke-width="1.4"><circle cx="8" cy="8" r="6.5"/><ellipse cx="8" cy="8" rx="3" ry="6.5"/><path d="M1.5 8h13"/></g></svg>
          www.getparcelkits.example
        </li>
      </ul>
    </div>
    <p class="address">4827 W. Ridge 418 S.Fort Worth, TX 73948</p>
  </section>

  <section class="card card-back" aria-label="Card back">
    <div class="brand"><span class="brand-square"></span>The Crate Heron</div>
  </section>
</main>
</body>
</html>
```